Briefpapier und Visitenkarten für Bayerisches Gasthaus mit Zimmer
Zielgruppe
Traditionelle Gaststätte im Zentrum einer Kleinstadt in Bayern. Direkt am Marktplatz. 10 Gästezimmer.
Bayerisch. Traditionell. Von junger Geschäftsführerin geführt, mit jungem Personal. Wir haben das Objekt erst vor Kurzem erworben und fangen gerade an.
Gerichte: Braten, Steaks, Brotzeiten, vegetarische und VEGANE Speisen
Getränke: Sehr bierlastig. Es war früher ein Brauereigasthaus. Heute gibts auch eine kleine feine Weinkarte.
Zielgruppe sind Einheimische und Touristen. Im Sommer kommen Radfahrer und Wanderer. Besonders angesprochen werden auch Kinder. Es gibt eine großzügige Spielecke.
Aufgabenstellung
Das Gasthaus heißt Eichel. Daher spielt der Eichel im Design auch eine wichtige Rolle.
Nachdem wir sehr familienorientiert sind, könnte ich mir auch eine Eichel-Familie vorstellen.
Visitenkarten und Briefpapier sollen alle wichtigen Infos enthalten, aber dabei sehr klar gehalten werden und nicht überladen sein. Mir ist ein schlichtes und ansprechendes Design wichtig. Es soll nicht verspielt sein.
Hier ist die Homepage:
www.eichel-gasthof-online.de
Info auf Briefpapier:
GASTHAUS EICHEL
Brennauer GmbH
Als Info auf Visitenkarte:
Gasthaus Eichel

```html
<!DOCTYPE html>
<html lang="de">
<head>
<meta charset="utf-8">
<title>Briefpapier – Gasthaus Eichel</title>
<link rel="stylesheet" href="https://fonts.googleapis.com/css2?family=Fira+Sans:wght@300;400&display=swap">
<style>
  :root {
    --paper: #ffffff;
    --ink: #6f6f72;
    --green: #9dc41f;
    --tint: #f3f6e8;
    --tint-fade: rgba(243, 246, 232, 0);
  }
  * { margin: 0; padding: 0; box-sizing: border-box; }
  html, body { width: 900px; height: 1200px; overflow: hidden; }
  body {
    background: var(--paper);
    font-family: "Fira Sans", Arial, sans-serif;
    font-weight: 300;
    color: var(--ink);
    position: relative;
  }
  .letterhead { position: absolute; inset: 0; }
  .decor-area { position: absolute; left: 0; top: 340px; width: 900px; height: 860px; }
  .brand {
    position: absolute; left: 645px; top: 120px; width: 172px;
    text-align: center;
  }
  .brand-dot {
    width: 34px; height: 34px; border-radius: 50%;
    background: var(--green); margin: 0 auto 14px;
  }
  .brand-name {
    font-size: 19px; font-weight: 300; letter-spacing: 3px; line-height: 22px;
    color: var(--ink);
  }
  .divider { position: absolute; left: 645px; width: 172px; height: 3px; display: flex; gap: 8px; }
  .divider span { flex: 1; background: var(--green); border-radius: 2px; height: 2px; }
  .divider.top-brand { top: 190px; }
  .divider.footer-start { top: 946px; left: 650px; }
  .divider.footer-end { top: 1172px; left: 650px; }
  .sender-line {
    position: absolute; left: 107px; top: 202px;
    font-size: 8px; letter-spacing: 0.2px; font-weight: 400;
  }
  .sender-line .sep { color: var(--green); margin: 0 2px; }
  .contact { position: absolute; left: 650px; top: 228px; font-size: 11px; letter-spacing: 0.6px; line-height: 16px; }
  .contact-row { position: relative; padding-left: 20px; }
  .contact-row svg { position: absolute; left: 0; top: 2px; width: 12px; height: 12px; fill: var(--green); }
  .contact-row + .contact-row { margin-top: 4px; }
  .contact-row.tight { margin-top: 0; }
  .fold-mark { position: absolute; left: 0; width: 22px; height: 1px; background: var(--green); }
  .legal { position: absolute; left: 670px; top: 956px; font-size: 11px; letter-spacing: 0.6px; line-height: 15.5px; }
  .legal p + p { margin-top: 5px; }
</style>
</head>
<body>
<main class="letterhead">
  <svg class="decor-area" role="img" aria-label="Große, zart getönte Hintergrundgrafik des Gasthaus-Symbols" viewBox="0 0 900 860" preserveAspectRatio="none">
    <defs>
      <linearGradient id="tintFade" x1="0" y1="0" x2="0" y2="1">
        <stop offset="0" stop-color="var(--tint)" stop-opacity="0"/>
        <stop offset="0.35" stop-color="#f3f6e8" stop-opacity="0.8"/>
        <stop offset="1" stop-color="#f3f6e8"/>
      </linearGradient>
    </defs>
    <rect width="900" height="860" fill="url(#tintFade)"/>
  </svg>

  <div class="brand">
    <div class="brand-dot"></div>
    <div class="brand-name">GASTHAUS<br>EICHEL</div>
  </div>
  <div class="divider top-brand"><span></span><span></span></div>

  <p class="sender-line">GASTHAUS EICHEL<span class="sep">•</span>Brennauer GmbH<span class="sep">•</span>Marktplatz 12<span class="sep">•</span>84123 Lindhofen</p>

  <address class="contact" style="font-style:normal">
    <div class="contact-row">
      <svg viewBox="0 0 12 12"><path d="M6 0a4 4 0 0 0-4 4c0 3 4 8 4 8s4-5 4-8a4 4 0 0 0-4-4zm0 5.6A1.6 1.6 0 1 1 6 2.4a1.6 1.6 0 0 1 0 3.2z"/></svg>
      GASTHAUS EICHEL<br><span style="display:block;margin-top:4px">Brennauer GmbH<br>Marktplatz 12<br>84123 Lindhofen</span>
    </div>
    <div class="contact-row">
      <svg viewBox="0 0 12 12"><path d="M2.5 0.5l2 2.2-1.2 1.6c.8 1.8 2.3 3.3 4.1 4.1l1.6-1.2 2.2 2-1.4 2.3C4.6 11 1 7.4.5 2z"/></svg>
      08765 4321
    </div>
    <div class="contact-row">
      <svg viewBox="0 0 12 12"><path d="M6 1a5 5 0 1 0 2.6 9.3l-.5-.9A4 4 0 1 1 10 6v.6c0 .6-.4 1-.9 1s-.9-.4-.9-1V3.5h-1v.4A2.4 2.4 0 1 0 7.6 8a1.9 1.9 0 0 0 3.4-1.4V6a5 5 0 0 0-5-5zm0 6.4A1.4 1.4 0 1 1 6 4.6a1.4 1.4 0 0 1 0 2.8z"/></svg>
      info@eichel-gasthof-online.de
    </div>
    <div class="contact-row tight">
      <svg viewBox="0 0 12 12"><path d="M6 .5a5.5 5.5 0 1 0 0 11 5.5 5.5 0 0 0 0-11zm3.8 5H8a8 8 0 0 0-.6-3.2 4.5 4.5 0 0 1 2.4 3.2zM6 1.6c.5.7 1 2.1 1 3.9H5c0-1.8.5-3.2 1-3.9zM4.6 2.3A8 8 0 0 0 4 5.5H2.2a4.5 4.5 0 0 1 2.4-3.2zM2.2 6.5H4a8 8 0 0 0 .6 3.2 4.5 4.5 0 0 1-2.4-3.2zM6 10.4c-.5-.7-1-2.1-1-3.9h2c0 1.8-.5 3.2-1 3.9zm1.4-.7A8 8 0 0 0 8 6.5h1.8a4.5 4.5 0 0 1-2.4 3.2z"/></svg>
      www.eichel-gasthof-online.de
    </div>
  </address>

  <div class="fold-mark" style="top:424px"></div>
  <div class="fold-mark" style="top:599px"></div>
  <div class="fold-mark" style="top:847px"></div>

  <div class="divider footer-start"><span></span><span></span></div>
  <section class="legal">
    <p>Steuernummer:<br>USt.-IdNr. DE xxx</p>
    <p>Handelsregister:<br>ORT</p>
    <p>Geschäftsführer:<br>Vorname Nachname</p>
    <p>Bank:<br>Musterbank</p>
    <p>IBAN DExx xxxx xxxx xxxx xxxx xx<br>BIC XXXXXXX 1XXX</p>
    <p>Kontoinhaber:<br>Brennauer GmbH</p>
  </section>
  <div class="divider footer-end"><span></span><span></span></div>
</main>
</body>
</html>
```